Design Fresh and modern brochure about hypnosis

We need a clean and modern brochure designed for our hypnosis center. I have text, a logo, and a single image. I'd like all placed in a tri-fold brochure with design elements added and I'd like the result in a format which can be modified, like InDesign. The brochure should appear modern and clean, but also with a softer look to appear compassionate. The company values are professional, compassionate, and local. Local is the Pacific Northwest. Colors should match the logo, blue with elements of water. I'd like to see shades of blue with white.
Updates

Hello designers. Thank you all for your great brochure designs thus far. 

At this time I've narrowed down the top 2 designs and those designers have been contacted. 

So right now, any new designs would be in consideration for third place. I want to be fair to your time, so please consider if you're still interested in submitting a design for 3rd place or not. 

Thank you. 

Target Market(s)

Adults in western US who want to improve their lives. Primarily 30+ in age, english speaking, and working full or part time.

Industry/Entity Type

It Company

Colors
85cae6
0555a3
3276b5
86cfc6
32b7a4

Requirements
Must have
• The brochure must include the logo and image attached, and should fit in the tri-fold design, similar to the example brochure. It also needs to be in a format that can be easily modified over time, as I typically change text in the brochure. InDesign would be great.
Nice to have
• Additional design elements - like areas for a call-out to highlight features.

```html
<!DOCTYPE html>
<html lang="en">
<head>
<meta charset="utf-8">
<title>Harbor Hypnosis Center – Tri-fold Brochure</title>
<link href="https://fonts.googleapis.com/css2?family=Cinzel:wght@400;500&family=Roboto+Condensed:wght@400&family=Open+Sans:wght@300;400;700&display=swap" rel="stylesheet">
<style>
  :root {
    --sky: #85cae6;
    --deep-blue: #0555a3;
    --mid-blue: #3276b5;
    --seafoam: #86cfc6;
    --teal: #32b7a4;
    --slate: #3b5d68;
    --ink: #1f1f1f;
    --white: #ffffff;
    --backdrop: #eef2f4;
  }
  * { box-sizing: border-box; margin: 0; padding: 0; }
  html, body { width: 1200px; height: 943px; overflow: hidden; background: var(--backdrop); }
  .canvas { position: relative; width: 1200px; height: 943px; }
  .brochure {
    position: absolute; left: 37px; top: 37px; width: 1126px; height: 868px;
    display: flex; box-shadow: 0 4px 14px rgba(0,0,0,.25); background: var(--white);
  }
  .panel { position: relative; height: 100%; }
  .heading {
    font-family: "Cinzel", serif; font-weight: 400; text-align: center; line-height: 1.1;
  }
  .copy {
    font-family: "Roboto Condensed", sans-serif; font-size: 15.3px; line-height: 20.5px;
    color: var(--ink); text-align: justify;
  }
  .copy p { margin-bottom: 11px; }

  /* Left panel */
  .panel--intro { width: 373px; background: linear-gradient(90deg, #ffffff 0%, #d8f0ec 30%, var(--seafoam) 100%); padding: 34px 32px 0 31px; }
  .panel--intro .heading { font-size: 22.5px; color: #1d3540; margin-bottom: 14px; }
  .panel--intro .heading--second { margin: 16px 0 13px; }

  /* Middle panel */
  .panel--services { width: 377px; }
  .services-band { height: 421px; background: var(--sky); padding: 24px 18px 0 26px; border-bottom: 3px solid var(--teal); }
  .services-band .heading { font-size: 21px; color: var(--deep-blue); text-align: center; margin-bottom: 18px; }
  .service-list { display: grid; grid-template-columns: 168px 1fr; list-style: none;
    font-family: "Roboto Condensed", sans-serif; font-size: 15.3px; line-height: 24.8px; color: var(--white); padding-left: 6px; }
  .service-list li::before { content: "• "; }
  .service-list li.more::before { content: ""; }
  .contact-note { padding: 12px 32px 0 34px; }
  .portrait { position: absolute; left: 82px; top: 523px; width: 218px; height: 198px;
    background: linear-gradient(180deg, #b9cfdc 0%, #8aa3ae 45%, #6b6a60 100%); box-shadow: 0 3px 8px rgba(0,0,0,.3); }
  .footer-info { position: absolute; left: 0; right: 0; top: 749px; text-align: center;
    font-family: "Roboto Condensed", sans-serif; font-size: 14.6px; line-height: 20.5px; color: var(--ink); }

  /* Right panel */
  .panel--cover { width: 376px; }
  .cover-header { height: 119px; background: var(--deep-blue); border-bottom: 5px solid #cfe6ea;
    display: flex; align-items: center; justify-content: center; padding-top: 4px; }
  .cover-header .heading { font-size: 26.5px; color: var(--white); line-height: 31px; }
  .tagline { margin-top: 20px; text-align: center; font-family: "Open Sans", sans-serif; font-weight: 300;
    font-size: 21px; line-height: 27px; color: var(--mid-blue); }
  .brand { margin-top: 52px; display: flex; align-items: center; justify-content: center; gap: 12px;
    font-family: "Open Sans", sans-serif; font-weight: 400; font-size: 22px; line-height: 28px; color: var(--mid-blue); }
  .brand .dot { width: 26px; height: 26px; border-radius: 50%; background: var(--sky); flex: none; }
  .pendulum { position: absolute; left: 28px; right: 0; top: 428px; height: 360px;
    background: radial-gradient(ellipse at 55% 80%, #d9b26a 0%, #efe3cf 22%, #ffffff 60%), #ffffff; }
  .cover-footer { position: absolute; left: 0; right: 0; bottom: 0; height: 80px; background: var(--slate);
    color: var(--white); text-align: center; font-family: "Open Sans", sans-serif; font-weight: 700; padding-top: 6px; }
  .cover-footer .phone { font-size: 25px; line-height: 30px; }
  .cover-footer .web { font-size: 19px; line-height: 24px; }
</style>
</head>
<body>
<div class="canvas">
  <div class="brochure">

    <section class="panel panel--intro">
      <h2 class="heading">Hypnosis can help you succeed when nothing else has worked!</h2>
      <div class="copy">
        <p>Hypnosis is one of the fastest growing fields of human achievement. As hypnotherapists we are working with people who are frustrated because nothing else has helped them achieve their goals.</p>
        <p>They have tried every other avenue that they can think of without success. We use hypnosis, hypnotherapy and teach self-hypnosis so that people like you can succeed in making important changes.</p>
        <p>Did you know that many of the most successful professional and Olympic teams use hypnosis to help their athletes win? That’s true.</p>
        <p>Now you can use this advantage for yourself, whether you are trying to overcome an old problem or if you want to grow to a new level of personal achievement.</p>
        <p>Hypnotherapy can also be used as a complementary treatment for some medical and psychological issues. We can contact your doctor to make sure that using hypnosis is appropriate for your situation.</p>
        <p>Appropriate issues may include pain management, stress related illness and any issue that has been labeled psychogenic in origin.</p>
      </div>
      <h2 class="heading heading--second">Hypnosis can be your tool for success!</h2>
      <div class="copy">
        <p>We encourage you to call or come into our office and ask us questions about hypnosis and our services. We enjoy answering questions. It is part of our job.</p>
      </div>
    </section>

    <section class="panel panel--services">
      <div class="services-band">
        <h2 class="heading">Hypnosis can help you with the following and more:</h2>
        <ul class="service-list">
          <li>Stop Smoking</li><li>Weight Loss</li>
          <li>Anxiety</li><li>Stress</li>
          <li>Remove Fears</li><li>Relationships</li>
          <li>Remove Habits</li><li>Childbirth</li>
          <li>Drug Abuse</li><li>Stage Fright</li>
          <li>Motivation</li><li>Pain Management</li>
          <li>Public Speaking</li><li>Sexual Issues</li>
          <li>Anger Issues</li><li>Self-Esteem</li>
          <li>Abuse Issues</li><li>Self-Confidence</li>
          <li>Concentration</li><li>Shyness</li>
          <li>Test Anxiety</li><li>Improve Mood</li>
          <li>Procrastination</li><li>Children’s Issues</li>
          <li>Improve Sports</li><li class="more">And, More…</li>
        </ul>
      </div>
      <div class="copy contact-note">
        <p>Contact our office for more information. Your hypnotherapist will be happy to tell you about appointment availability and fees for services.</p>
      </div>
      <div class="portrait" role="img" aria-label="Portrait photo of the hypnotherapist by the shore"></div>
      <div class="footer-info">
        (555) 014-2290<br>
        HarborHypnosisCenter.com<br>
        Copyright © 2014 Harbor Hypnosis Center.<br>
        All rights reserved.<br>
        HarborHypnosisCenter.com
      </div>
    </section>

    <section class="panel panel--cover">
      <header class="cover-header">
        <h1 class="heading">Hypnosis and<br>Hypnotherapy<br>Information</h1>
      </header>
      <p class="tagline">Learn how hypnosis and<br>hypnotherapy can help you<br>succeed.</p>
      <div class="brand">
        <span class="dot"></span>
        <span class="name">Harbor Hypnosis Center</span>
      </div>
      <div class="pendulum" role="img" aria-label="Photo of a hand swinging a gold pocket watch on a chain"></div>
      <footer class="cover-footer">
        <div class="phone">(555) 014-2290</div>
        <div class="web">HarborHypnosisCenter.com</div>
      </footer>
    </section>

  </div>
</div>
</body>
</html>
```